Clean Landing Page - Design and Code

Need to create a similar landing page to example i have supplied. Need versions for Desktop, tablet and mobile. Letting the design chose color scheme based on description.

We want it to seem fresh, clean and cool.

We are basing it off this example http://corvenhalt.com/

Target Market(s)

young ambitious entreprerial women

Coding

Coded - Design and coding required

Number of Pages Required

3 page

Font styles to use
Sans Serif

Requirements
Must have
• Must be designed for responsive functionality.

```html
<!DOCTYPE html>
<html lang="en">
<head>
<meta charset="utf-8">
<title>Mara Kessling – Paid Social Media Influencer Guide</title>
<link href="https://fonts.googleapis.com/css2?family=Raleway:wght@200;300;700&family=Open+Sans:wght@300;400;600;700&display=swap" rel="stylesheet">
<style>
  :root{
    --plum:#3d1a26;
    --plum-deep:#2c121a;
    --slate:#4b4b4d;
    --white:#ffffff;
    --ink:#222222;
    --nav-text:#777777;
    --heart:#c0392b;
  }
  *{margin:0;padding:0;box-sizing:border-box}
  html,body{width:1200px;height:1019px;overflow:hidden;background:var(--white)}
  body{position:relative;font-family:"Open Sans",sans-serif;color:var(--white)}

  .topbar{position:absolute;left:0;top:0;width:1200px;height:50px;background:var(--white);border-bottom:1px solid #e6e6e6}
  .brand{position:absolute;left:93px;top:14px;font-size:16px;color:var(--nav-text);letter-spacing:.2px}
  .nav{position:absolute;right:103px;top:16px;display:flex;gap:27px;font-size:13px;color:var(--nav-text)}
  .nav .caret{display:inline-block;margin-left:5px;border-left:4px solid transparent;border-right:4px solid transparent;border-top:4px solid var(--nav-text);vertical-align:middle}

  .hero{position:absolute;left:0;top:50px;width:1200px;height:906px;background:var(--plum);overflow:hidden}
  .portrait{position:absolute;left:0;top:0;width:600px;height:906px;
    background:linear-gradient(180deg,#8d8f94 0%,#77787c 45%,#5d5b5d 100%)}

  .headline{position:absolute;left:614px;top:22px;width:580px;font-family:"Raleway",sans-serif;font-weight:200;font-size:52px;line-height:55px;letter-spacing:-.3px}
  .lede{position:absolute;left:614px;top:204px;width:570px;font-size:17px;line-height:25px;font-weight:300}

  .feature{position:absolute;display:flex;align-items:center;background:var(--plum-deep)}
  .feature .icon{display:flex;align-items:center;justify-content:center;height:100%;flex:none}
  .feature .label{font-family:"Raleway",sans-serif;font-weight:200;font-size:23.5px;line-height:27px}
  .feature.wide{left:600px;top:280px;width:600px;height:92px}
  .feature.wide .icon{width:100px}
  .feature.wide .label{padding-left:14px;padding-right:20px}
  .feature.inset .icon{width:89px;background:var(--slate)}
  .feature.inset .label{padding-left:25px;padding-right:14px}
  .f-mail{left:511px;top:377px;width:600px;height:92px}
  .f-price{left:511px;top:475px;width:600px;height:66px}
  .f-brands{left:519px;top:545px;width:599px;height:66px}

  .cta{position:absolute;left:338px;top:683px;width:523px;height:65px;background:var(--white);border-radius:18px;
    display:flex;align-items:center;justify-content:center;color:var(--ink);font-weight:600;font-size:20px;letter-spacing:2.6px}

  .social{position:absolute;left:0;top:797px;width:1200px;display:flex;justify-content:center;gap:20px;font-size:12px;font-weight:700}
  .tagline{position:absolute;left:0;top:830px;width:1200px;text-align:center;font-family:"Raleway",sans-serif;font-weight:300;font-size:36px}
  .tagline strong{font-weight:700}

  .footer{position:absolute;left:0;top:956px;width:1200px;height:63px;background:var(--white);color:var(--ink);font-size:10px;font-weight:700}
  .footer .copy{position:absolute;left:93px;top:27px}
  .footer .made{position:absolute;right:95px;top:27px}
  .footer .heart{color:var(--heart)}
</style>
</head>
<body>
  <header class="topbar">
    <div class="brand">MARA KESSLING</div>
    <nav class="nav"><span>HOME</span><span>MENU<span class="caret"></span></span></nav>
  </header>

  <section class="hero">
    <div class="portrait" role="img" aria-label="Portrait photo of the smiling host in a white lace top against a pale wall"></div>

    <h1 class="headline">The Advanced Guide to Becoming a Paid Social Media Influencer</h1>
    <p class="lede">We don't want to overload you with hundreds of styles you don't want, or need. We give you a strong base to express your own creativity.</p>

    <div class="feature wide">
      <div class="icon">
        <svg width="42" height="38" viewBox="0 0 42 38" fill="none" stroke="#fff" stroke-width="4" stroke-linecap="round" stroke-linejoin="round">
          <path d="M30 20v10a4 4 0 0 1-4 4H8a4 4 0 0 1-4-4V12a4 4 0 0 1 4-4h16"/>
          <path d="M11 18l7 7L38 5"/>
        </svg>
      </div>
      <div class="label">The Little-Known Secrets to Grow a Highly Engaged Following</div>
    </div>

    <div class="feature inset f-mail">
      <div class="icon">
        <svg width="40" height="30" viewBox="0 0 40 30" fill="none" stroke="#fff" stroke-width="3.5" stroke-linejoin="round">
          <rect x="2" y="2" width="36" height="26" rx="3"/>
          <path d="M3 5l17 13L37 5"/>
        </svg>
      </div>
      <div class="label">How to properly contact brands via DM and Email</div>
    </div>

    <div class="feature inset f-price">
      <div class="icon">
        <svg width="42" height="28" viewBox="0 0 42 28">
          <rect x="1" y="1" width="40" height="26" fill="#fff"/>
          <rect x="5" y="5" width="32" height="18" fill="#4b4b4d"/>
          <circle cx="21" cy="14" r="8" fill="#fff"/>
          <text x="21" y="18.5" text-anchor="middle" font-family="Open Sans, sans-serif" font-weight="700" font-size="12" fill="#4b4b4d">1</text>
        </svg>
      </div>
      <div class="label">How to Negotiate your price per post.</div>
    </div>

    <div class="feature inset f-brands">
      <div class="icon">
        <svg width="42" height="36" viewBox="0 0 42 36" fill="#fff">
          <path d="M2 4v12l18 18 14-14L16 2H4a2 2 0 0 0-2 2z"/>
          <circle cx="9" cy="9" r="3" fill="#4b4b4d"/>
          <path d="M21 2h4l16 16-14 14-2-2 12-12z"/>
        </svg>
      </div>
      <div class="label">How to Attract Brands to your Feed</div>
    </div>

    <div class="cta">YES, I WANT MARA TO SHOW ME HOW</div>

    <div class="social"><span>Vell</span><span>Onda</span><span>Pixa</span><span>Tovi</span><span>Brel</span><span>Zuma</span></div>
    <p class="tagline">Kickstart your Startup with <strong>Mara</strong></p>
  </section>

  <footer class="footer">
    <div class="copy">© Kessling Studio - MARA KESSLING</div>
    <div class="made">Made with <span class="heart">♥</span> Mara</div>
  </footer>
</body>
</html>
```